Solar appointment reminder card

We are looking for a new design for our appointment reminder card since we have changed our logo. The card should have the new logo along with space for the employee to hand write the customers appointment date, time, the employees name and phone number.
I've uploaded what our old basic appointment card looked like and our new logo.

The cards should be in a standard business card size and could be horizontal or vertical.

```html
<!DOCTYPE html>
<html lang="en">
<head>
<meta charset="utf-8">
<title>Sunhaven Power – Appointment Card</title>
<link rel="stylesheet" href="https://fonts.googleapis.com/css2?family=Open+Sans:wght@600;800&display=swap">
<style>
  :root {
    --backdrop: #f0f0f0;
    --paper: #ffffff;
    --sun-yellow: #fdd03f;
    --sun-yellow-deep: #fccf3a;
    --brand-orange: #f7983a;
    --ink-light: #ffffff;
  }
  * { box-sizing: border-box; margin: 0; padding: 0; }
  html, body {
    width: 1200px; height: 900px; overflow: hidden;
    background: var(--backdrop);
    font-family: "Open Sans", Arial, sans-serif;
  }
  .card {
    position: absolute;
    top: 340px;
    width: 392px; height: 224px;
    background: var(--paper);
    overflow: hidden;
  }
  .card--front {
    left: 169px;
    border: 7px solid var(--sun-yellow);
    display: flex; align-items: center; justify-content: center;
  }
  .card--back { left: 638px; }

  .brand {
    display: flex; align-items: center;
    color: var(--brand-orange);
    font-weight: 800;
  }
  .brand__dot {
    border-radius: 50%;
    background: var(--sun-yellow);
    flex: none;
  }
  .brand__name { line-height: 1.02; }

  .card--front .brand { gap: 14px; }
  .card--front .brand__dot { width: 62px; height: 62px; }
  .card--front .brand__name { font-size: 38px; }

  .card--back .brand {
    position: absolute; left: 18px; top: 84px; gap: 7px;
  }
  .card--back .brand__dot { width: 26px; height: 26px; }
  .card--back .brand__name { font-size: 17px; }

  .appointment-panel {
    position: absolute; inset: 0;
    width: 392px; height: 224px;
  }
  .appointment__title {
    position: absolute; left: 234px; top: 14px;
    color: var(--ink-light);
    font-weight: 600; font-size: 19px;
  }
  .appointment__fields {
    position: absolute; left: 182px; top: 62px;
    list-style: none;
    color: var(--ink-light);
    font-weight: 600; font-size: 13.5px;
  }
  .appointment__field { height: 34.5px; }
</style>
</head>
<body>

  <section class="card card--front">
    <div class="brand">
      <span class="brand__dot"></span>
      <span class="brand__name">Sunhaven<br>Power</span>
    </div>
  </section>

  <section class="card card--back">
    <svg class="appointment-panel" viewBox="0 0 392 224" aria-hidden="true">
      <defs>
        <linearGradient id="panelFill" x1="0" y1="0" x2="1" y2="1">
          <stop offset="0" stop-color="var(--sun-yellow)"/>
          <stop offset="1" stop-color="var(--sun-yellow-deep)"/>
        </linearGradient>
      </defs>
      <path d="M203,0 H392 V224 H174 Q136,120 203,0 Z" fill="url(#panelFill)"/>
    </svg>

    <div class="brand">
      <span class="brand__dot"></span>
      <span class="brand__name">Sunhaven<br>Power</span>
    </div>

    <h2 class="appointment__title">Appointment</h2>
    <ul class="appointment__fields">
      <li class="appointment__field">Date:</li>
      <li class="appointment__field">Time:</li>
      <li class="appointment__field">Representative:</li>
      <li class="appointment__field">Phone:</li>
    </ul>
  </section>

</body>
</html>
```